Plakat für Fensterbau-Meisterbetrieb
Zielgruppe
Wir sind ein Fensterbau-Meisterbetrieb und überwiegend in der Modernisierung, Restaurierung und Instandhaltung tätig. Unsere Zielgruppe sind in unserer Region alle die Interesse an neuen Fenstern/Haustüren usw. haben.
Aufgabenstellung
Gesucht wird ein Design für ein Gerüst-Plakat, die Maße sind in den Anhängen. Das Design sollte an dem Bestehenden Firmenlogo/Website angeglichen sein. Ein kurzer Werbespruch 'Fenster die begeistern!' sollte auf dem Plakat zu finden sein. Die Homepage, Adresse (Am Lindenbühl 7, 79312 Bruchsal) und ganz Wichtig das Firmenlogo sollte ebenfalls vertreten sein.
Ansonsten lassen wir uns gerne von Kreativen Vorschlägen überraschen. =)
Ein Briefbogen zur Orientierung ist ebenfalls im Anhang.
Nachtrag zu den Vorgaben:
Das Firmenlogo sollte der „eyecatcher“ sein und der Werbespruch eher Nebensache.
Schriftart: MavenPro / MavenRegular

```html
<!DOCTYPE html>
<html lang="de">
<head>
<meta charset="utf-8">
<title>Hellwanger Glas- und Fenstertechnik – Gerüstplakat</title>
<link rel="stylesheet" href="https://fonts.googleapis.com/css2?family=Maven+Pro:wght@400;500;600;700&display=swap">
<style>
  :root {
    --page: #ffffff;
    --panel: #ffffff;
    --ink-dark: #545456;
    --ink-grey: #6f6f72;
    --brand-green: #7ab51d;
    --glass-light: #e4efc4;
    --glass-mid: #6fb52a;
    --glass-deep: #0d4a2c;
    --glass-teal: #1f8f86;
    --fade-grey: #e9eeeb;
  }
  html, body {
    margin: 0;
    padding: 0;
    width: 1200px;
    height: 1200px;
    overflow: hidden;
    background: var(--page);
  }
  .poster {
    position: absolute;
    left: 120px;
    top: 110px;
    width: 967px;
    height: 989px;
    display: block;
  }
  .poster text { font-family: "Maven Pro", sans-serif; }
  .brand-name { fill: var(--ink-dark); font-weight: 700; font-size: 94px; }
  .brand-descriptor { fill: var(--ink-grey); font-weight: 400; font-size: 44px; }
  .slogan { fill: var(--brand-green); font-weight: 600; font-size: 34px; }
  .contact-title { fill: var(--brand-green); font-weight: 700; font-size: 29px; }
  .contact-line { fill: var(--ink-dark); font-weight: 500; font-size: 29px; }
  .icon { fill: none; stroke: var(--brand-green); stroke-width: 2.2; stroke-linecap: round; stroke-linejoin: round; }
  .icon-solid { fill: var(--brand-green); }
</style>
</head>
<body>
<svg class="poster" viewBox="0 0 967 989" xmlns="http://www.w3.org/2000/svg">
  <defs>
    <linearGradient id="glass-facade" x1="0.35" y1="0" x2="0" y2="1">
      <stop offset="0" stop-color="var(--glass-light)"/>
      <stop offset="0.35" stop-color="var(--glass-mid)"/>
      <stop offset="0.7" stop-color="var(--glass-deep)"/>
      <stop offset="1" stop-color="var(--glass-teal)"/>
    </linearGradient>
    <linearGradient id="panel-fade" x1="0.5" y1="0.3" x2="1" y2="0.65">
      <stop offset="0" stop-color="var(--panel)"/>
      <stop offset="1" stop-color="var(--fade-grey)"/>
    </linearGradient>
    <linearGradient id="footer-fade" x1="0" y1="0" x2="1" y2="0">
      <stop offset="0" stop-color="var(--glass-deep)"/>
      <stop offset="0.55" stop-color="#dfe6e2"/>
      <stop offset="1" stop-color="#b9c4bf"/>
    </linearGradient>
  </defs>

  <!-- Background photo area -->
  <rect class="facade-photo" x="0" y="0" width="967" height="989" fill="url(#glass-facade)"
        role="img" aria-label="Foto: moderne Glasfassade eines Hochhauses in Grüntönen"/>
  <rect class="facade-photo-footer" x="420" y="906" width="547" height="83" fill="url(#footer-fade)"
        role="img" aria-label="Foto: Glasfassade, hell auslaufend"/>

  <!-- White content panel -->
  <polygon class="content-panel" points="395,0 967,0 967,906 264,906 29,366" fill="url(#panel-fade)"/>
  <rect class="contact-panel" x="264" y="638" width="703" height="268" fill="var(--panel)"/>

  <!-- Brand -->
  <text class="brand-name" x="161" y="391" textLength="731" lengthAdjust="spacingAndGlyphs">Hellwanger</text>
  <text class="brand-descriptor" x="215" y="441" textLength="677" lengthAdjust="spacing">GLAS- UND FENSTERTECHNIK</text>

  <!-- Slogan -->
  <text class="slogan" x="511" y="512" textLength="368" lengthAdjust="spacingAndGlyphs">Fenster die begeistern!</text>

  <!-- Contact block -->
  <text class="contact-title" x="314" y="716" textLength="590" lengthAdjust="spacingAndGlyphs">Hellwanger Glas - und Fenstertechnik</text>

  <g class="contact-icon pin" transform="translate(320,752)">
    <path class="icon-solid" d="M0,-11 a8,8 0 0 1 8,8 c0,6 -8,13 -8,13 c0,0 -8,-7 -8,-13 a8,8 0 0 1 8,-8z"/>
    <circle cx="0" cy="-3" r="3" fill="var(--panel)"/>
  </g>
  <text class="contact-line" x="345" y="762">Am Lindenbühl 7&#160;&#160;79312 Bruchsal</text>

  <g class="contact-icon phone" transform="translate(320,790)">
    <path class="icon-solid" d="M-8,-9 l5,-2 l4,7 l-3,3 c1,4 4,7 8,8 l3,-3 l7,4 l-2,5 c-12,1 -23,-10 -22,-22z"/>
  </g>
  <text class="contact-line" x="345" y="799">0151-4429376</text>

  <g class="contact-icon globe" transform="translate(320,825)">
    <circle class="icon" cx="0" cy="0" r="10"/>
    <ellipse class="icon" cx="0" cy="0" rx="4.5" ry="10"/>
    <line class="icon" x1="-10" y1="0" x2="10" y2="0"/>
    <line class="icon" x1="-8.5" y1="-5" x2="8.5" y2="-5"/>
    <line class="icon" x1="-8.5" y1="5" x2="8.5" y2="5"/>
  </g>
  <text class="contact-line" x="345" y="834" textLength="552" lengthAdjust="spacingAndGlyphs">www.hellwanger-fenstertechnik.de</text>

  <g class="contact-icon mail" transform="translate(320,862)">
    <rect class="icon" x="-10" y="-7" width="20" height="14"/>
    <polyline class="icon" points="-10,-7 0,2 10,-7"/>
  </g>
  <text class="contact-line" x="345" y="871" textLength="552" lengthAdjust="spacingAndGlyphs">info@hellwanger-fenstertechnik.de</text>
</svg>
</body>
</html>
```